TotHaven Community Landing Page

TotHaven is a virtual world built with childrens' needs in mind. It is an online portal where parents will find all kids' related stuffs and a community connect point for parents to interact and share their experiences.

We need the designs for 2 pages within TotHaven:
- Landing Page for the Community Area
- Registration page for membership

1) The Landing Page need to have the following:

Logo & Main Background :- use the images attached

Page Title & Navigation Menu :-
The page title is "Community Connect"; navigation menu should be able to hold at least 6 tabs

Login Widget* :-
We want to put emphasis on the design of this.
For visitors, this is a normal login widget with username/password input fields, register button and 'login with chatterbook' button.
For logged-in users, this becomes a simple dashboard widget with Avatar, shortlinks and some useful navigation buttons.

"Groups" Section :-
This area holds an image, a short paragraph introducing "Groups", a widget showing 5-10 latest/popular groups and a 'Go to Groups' button at the bottom.

"Forum" Section :-
This area holds an image, a short paragraph introducing "Forum", a widget showing 5-10 latest/popular discussion topics and a 'Go to Forum' button at the bottom.

"Activities" Section -
This area holds an image, a short paragraph introducing "Forum", a widget showing 5-10 latest/popular events & activities and a 'Go to Activities' button at the bottom.

"Marketplace" Section :-
This area holds an image, a short paragraph introducing "Marketplace", a widget showing 5-10 latest/popular products and a 'Go to Marketplace' button at the bottom.

Social Media elements :-
The usual social media icons and chatterbook like box.

2) The Registration Page will need to contain the registration form as per the image attached.

Target Market(s)

Parents with kids ranging from 2 - 12 years old

Industry/Entity Type

Events

Requirements
Nice to have
• - colorful illustrations of kids or kids related images all around

```html
<!DOCTYPE html>
<html lang="en">
<head>
<meta charset="utf-8">
<title>TotHaven – Community Connect</title>
<link href="https://fonts.googleapis.com/css2?family=Arimo:wght@400;700&family=Comfortaa:wght@400&display=swap" rel="stylesheet">
<style>
:root{
  --sky-top:#2f9fd8;
  --sky-mid:#8fd4f2;
  --grass-light:#8cc63f;
  --grass-dark:#3f7f1c;
  --panel:#ffffff;
  --text:#333333;
  --muted:#555555;
  --orange:#f7941d;
  --orange-dark:#e8720c;
  --teal:#1fa3b5;
  --teal-dark:#148796;
  --link:#1b8fd1;
  --green-head:#2a6f8f;
  --footer-bg:#f3efe0;
  --line:#e3e3e3;
  --field:#f7f7f7;
  --chat:#3b5a9a;
}
*{box-sizing:border-box;margin:0;padding:0}
html,body{width:859px;height:1200px;overflow:hidden}
body{position:relative;font-family:"Arimo",Arial,sans-serif;color:var(--text);font-size:10px;background:var(--footer-bg)}
.abs{position:absolute}
.scenery{left:0;top:0;width:859px;height:1026px;
  background:linear-gradient(180deg,var(--sky-top) 0%,var(--sky-mid) 28%,#dff3fb 38%,var(--grass-light) 52%,#5aa12a 75%,var(--grass-dark) 100%)}
/* header */
.brand{left:120px;top:18px;display:flex;align-items:center;gap:8px}
.brand-mark{width:26px;height:26px;border-radius:50%;background:#fff}
.brand-name{font-weight:700;font-size:34px;color:#fff}
.account-links{right:225px;top:20px;font-size:10px;color:#444;white-space:nowrap}
.account-links span{margin:0 5px}
.social{top:14px;width:22px;height:22px;border-radius:3px}
.nav{top:53px;height:24px;display:flex;gap:6px;left:341px}
.nav a{display:block;height:24px;line-height:24px;text-align:center;color:#fff;font-size:11px;text-decoration:none;border-radius:2px;background:var(--teal)}
.nav a.active{background:var(--orange)}
/* hero */
.hero{left:118px;top:92px;width:462px;height:208px;background:linear-gradient(180deg,#9fd3ef 0%,#d8a07a 40%,#6fae3b 70%,#3f8a21 100%);border:2px solid #fff}
.hero-caption{left:118px;top:224px;width:208px;height:54px;background:rgba(242,140,30,.85);color:#fff;font-size:15px;padding:8px 10px;line-height:19px}
.hero-pager{left:510px;top:263px;color:#fff;font-size:24px;letter-spacing:6px;font-weight:700}
/* login */
.login{left:586px;top:92px;width:160px;height:208px;background:#fff;border:1px solid #ddd}
.login-head{height:32px;background:linear-gradient(var(--orange),var(--orange-dark));color:#fff;font-weight:700;font-size:11px;line-height:32px;padding-left:12px}
.field{position:absolute;left:6px;width:146px;height:24px;border:1px solid #ccc;background:#fff;display:flex;align-items:center}
.field i{width:22px;height:22px;background:#ddd;margin-right:8px}
.field span{color:#555;font-size:9.5px}
.remember{position:absolute;left:8px;top:105px;font-size:8px;color:#444;display:flex;align-items:center;gap:4px}
.remember b{width:9px;height:9px;border:1px solid #888}
.forgot{position:absolute;right:6px;top:105px;font-size:8.5px;color:var(--link);text-decoration:underline}
.btn-login{position:absolute;left:12px;top:133px;width:136px;height:25px;background:linear-gradient(#3cc3d6,var(--teal-dark));color:#fff;font-weight:700;font-size:11px;text-align:center;line-height:25px;border-radius:2px}
.btn-chat{position:absolute;left:12px;top:166px;width:136px;height:25px;background:var(--chat);color:#fff;font-weight:700;font-size:9.5px;line-height:25px;padding-left:10px;border-radius:2px}
/* panel */
.panel{left:118px;top:314px;width:628px;height:700px;background:var(--panel);border-radius:6px;box-shadow:0 0 6px rgba(0,0,0,.2)}
.page-title{left:136px;top:333px;font-family:"Comfortaa",sans-serif;font-size:21px;font-weight:400;color:var(--orange);white-space:nowrap}
.intro{left:136px;top:366px;width:400px;font-size:11px;line-height:14px;color:#222}
.photo{border:3px solid #fff;box-shadow:0 0 3px rgba(0,0,0,.35)}
.section-head{font-size:12.5px;font-weight:700;color:var(--green-head);border-bottom:1px solid #f3c48a;padding-bottom:3px}
.blurb{font-size:9px;line-height:14.5px;color:#222}
.sub-head{font-size:11.5px;color:#2bb3cd}
.sub-head.orange{color:var(--orange);font-weight:700;font-size:10px}
.link{font-size:9px;color:var(--link);text-decoration:underline}
.bullet{display:flex;align-items:center;gap:6px}
.bullet svg{flex:none}
.date{font-size:8px;color:#222}
.btn{height:26px;line-height:26px;text-align:center;color:#fff;font-size:11px;border-radius:2px;background:linear-gradient(var(--orange),var(--orange-dark))}
.divider{left:430px;top:456px;width:1px;height:540px;background:var(--line)}
.thumb{border:2px solid #fff;box-shadow:0 0 3px rgba(0,0,0,.35)}
.activity-list .link{font-size:8.5px;text-decoration:none;white-space:nowrap}
/* footer */
.footer{left:0;top:1026px;width:859px;height:174px;background:var(--footer-bg)}
.footer-kid{left:128px;top:1040px;width:42px;height:130px;background:linear-gradient(#f0c9a0,#5b8fc9);border-radius:14px}
.newsletter{left:166px;top:1056px;width:134px;height:94px;background:#fff;box-shadow:0 0 3px rgba(0,0,0,.2);padding:12px 6px}
.newsletter h4{font-weight:400;color:var(--orange);font-size:11px}
.newsletter .input{margin-top:10px;width:104px;height:16px;border:1px solid #bbb}
.newsletter .submit{margin-top:8px;width:46px;height:15px;background:#c8e07a;border:1px solid #7c9a2a;font-size:8.5px;text-align:center;line-height:13px}
.foot-col h5{color:var(--orange);font-weight:400;font-size:10px;margin-bottom:10px}
.foot-col p{font-size:8.5px;color:#222;margin-bottom:9px}
.likebox{left:562px;top:1037px;width:168px;height:133px;background:#fff;border:1px solid #ccc;padding:6px}
.likebox .top{display:flex;gap:8px}
.likebox .mini{width:48px;height:30px;background:var(--orange)}
.likebox b{font-size:10.5px;color:#333}
.like-btn{margin-top:3px;width:36px;height:13px;border:1px solid #aaa;font-size:8px;text-align:center;line-height:11px;background:#f2f2f2}
.likebox .count{font-size:8px;margin:6px 0 3px 12px;color:#333}
.likebox .count em{font-style:normal;color:var(--chat);font-size:10px}
.faces{display:grid;grid-template-columns:repeat(5,27px);gap:2px;margin-left:10px}
.faces i{height:27px;background:#8d8f93}
.copyright{left:118px;top:1184px;font-size:8px;color:#3a6fd6}
.grass-strip{left:0;top:1168px;width:859px;height:32px;background:linear-gradient(transparent,#9ccf5a)}
</style>
</head>
<body>
<div class="abs scenery" role="img" aria-label="Illustrated background: blue sky with clouds and rolling green hills"></div>

<header>
  <div class="abs brand"><span class="brand-mark"></span><span class="brand-name">TotHaven</span></div>
  <div class="abs account-links">My Account<span>|</span>Register</div>
  <div class="abs social" style="left:644px;background:#f7941d"></div>
  <div class="abs social" style="left:670px;background:#e8508f"></div>
  <div class="abs social" style="left:696px;background:#2aa9e0"></div>
  <div class="abs social" style="left:722px;background:#3b5a9a"></div>
  <nav class="abs nav">
    <a class="active" href="#" style="width:61px">Home</a>
    <a href="#" style="width:62px">About us</a>
    <a href="#" style="width:64px">Activities</a>
    <a href="#" style="width:62px">Blog</a>
    <a href="#" style="width:62px">Gallery</a>
    <a href="#" style="width:63px">Contact us</a>
  </nav>
</header>

<div class="abs hero" role="img" aria-label="Photo of smiling children lying on green grass"></div>
<div class="abs hero-caption">Lorem Ipsum. Proin gravida nibh vel velit auctor</div>
<div class="abs hero-pager">123</div>

<aside class="abs login">
  <div class="login-head">Please Log In</div>
  <div class="field" style="top:46px"><i></i><span>Username</span></div>
  <div class="field" style="top:75px"><i></i><span>Password</span></div>
  <div class="remember"><b></b>Remember Me</div>
  <div class="forgot">Forgot Password ?</div>
  <div class="btn-login">Log in</div>
  <div class="btn-chat">Login with chatterbook</div>
</aside>

<main>
  <div class="abs panel"></div>
  <h1 class="abs page-title">Welcome to Community Connect</h1>
  <p class="abs intro">Lorem Ipsum. Proin gravida nibh vel velit auctor aliquet. Aenean sollicitudin, lorem quis bibendum auctor, nisi elit consequat ipsum, nec sagittis sem nibh id elit. Duis sed odio sit amet nibh vulputate Lorem Ipsum.</p>
  <div class="abs photo" style="left:556px;top:329px;width:171px;height:115px;background:linear-gradient(#e9eef3,#cfe3f0)" role="img" aria-label="Photo of a girl holding a colourful sign"></div>

  <div class="abs divider"></div>

  <!-- Groups -->
  <h2 class="abs section-head" style="left:136px;top:440px;width:279px">Groups</h2>
  <p class="abs blurb" style="left:136px;top:477px;width:160px">Lorem Ipsum. Proin gravida nibh vel velit auctor aliquet. Aenean sollicitudin, lorem quis bibendum auctor, nisi elit consequat ipsum,</p>
  <div class="abs photo" style="left:301px;top:468px;width:114px;height:86px;background:linear-gradient(135deg,#f06d3b,#3fb0c9,#f2d23c)" role="img" aria-label="Photo of children lying in a circle"></div>
  <h3 class="abs sub-head" style="left:136px;top:544px">Latest Groups</h3>
  <div class="abs" style="left:140px;top:568px;display:grid;grid-template-columns:150px 120px;row-gap:6px">
    <div class="bullet"><svg width="8" height="8"><path d="M0 2h4V0l4 4-4 4V6H0z" fill="#f7941d"/></svg><span class="link">Lorem Ipsum. Proin gravida</span></div>
    <div class="bullet"><svg width="8" height="8"><path d="M0 2h4V0l4 4-4 4V6H0z" fill="#f7941d"/></svg><span class="link">Lorem Ipsum. Proin</span></div>
    <div class="bullet"><svg width="8" height="8"><path d="M0 2h4V0l4 4-4 4V6H0z" fill="#f7941d"/></svg><span class="link">Lorem Ipsum. Proin gravida</span></div>
    <div class="bullet"><svg width="8" height="8"><path d="M0 2h4V0l4 4-4 4V6H0z" fill="#f7941d"/></svg><span class="link">Lorem Ipsum</span></div>
    <div class="bullet"><svg width="8" height="8"><path d="M0 2h4V0l4 4-4 4V6H0z" fill="#f7941d"/></svg><span class="link">Lorem Ipsum</span></div>
    <div class="bullet"><svg width="8" height="8"><path d="M0 2h4V0l4 4-4 4V6H0z" fill="#f7941d"/></svg><span class="link">Lorem Ipsum. Proin</span></div>
    <div class="bullet"><svg width="8" height="8"><path d="M0 2h4V0l4 4-4 4V6H0z" fill="#f7941d"/></svg><span class="link">Lorem Ipsum. Proin gravida</span></div>
  </div>
  <div class="abs btn" style="left:301px;top:644px;width:96px">Go to Groups</div>

  <!-- Activities -->
  <h2 class="abs section-head" style="left:136px;top:691px;width:279px">Activities</h2>
  <div class="abs photo" style="left:136px;top:720px;width:151px;height:82px;background:linear-gradient(90deg,#e9a0a8,#e8e3dc,#9a6b5a)" role="img" aria-label="Photo of children playing indoors"></div>
  <p class="abs blurb" style="left:295px;top:722px;width:125px">Lorem Ipsum. Proin gravida nibh vel velit auctor aliquet. Aenean sollicitudin, lorem quis bibendum auctor, nisi elit consequat ipsum,</p>
  <h3 class="abs sub-head orange" style="left:136px;top:810px">Recent Activities</h3>
  <div class="abs activity-list" style="left:138px;top:832px;width:280px">
    <div class="bullet"><svg width="8" height="8"><path d="M0 2h4V0l4 4-4 4V6H0z" fill="#1fa3b5"/></svg><span class="link">Lorem Ipsum. Proin gravida nibh vel velit Lorem Ipsum. Proin gravida</span></div>
    <div class="date" style="margin:4px 0 10px 14px">July 19, 2013</div>
    <div class="bullet"><svg width="8" height="8"><path d="M0 2h4V0l4 4-4 4V6H0z" fill="#1fa3b5"/></svg><span class="link">Lorem Ipsum. Proin gravida nibh vel velit Lorem Ipsum.</span></div>
    <div class="date" style="margin:4px 0 10px 14px">July 19, 2013</div>
    <div class="bullet"><svg width="8" height="8"><path d="M0 2h4V0l4 4-4 4V6H0z" fill="#1fa3b5"/></svg><span class="link">Lorem Ipsum. Proin gravida nibh vel velit Lorem Ipsum. Proin gravida</span></div>
    <div class="date" style="margin:4px 0 10px 14px">July 19, 2013</div>
    <div class="bullet"><svg width="8" height="8"><path d="M0 2h4V0l4 4-4 4V6H0z" fill="#1fa3b5"/></svg><span class="link">Lorem Ipsum. Proin gravida nibh vel velit Lorem</span></div>
    <div class="date" style="margin:4px 0 0 14px">July 19, 2013</div>
  </div>
  <div class="abs btn" style="left:136px;top:959px;width:108px">Go to Activities</div>

  <!-- Forum -->
  <h2 class="abs section-head" style="left:445px;top:440px;width:282px">Forum</h2>
  <div class="abs photo" style="left:446px;top:467px;width:174px;height:85px;background:linear-gradient(90deg,#e65a4a,#6fa7dc,#5fbf5a)" role="img" aria-label="Illustration of figures around a globe"></div>
  <p class="abs blurb" style="left:628px;top:472px;width:104px;line-height:13.5px">Lorem Ipsum. Proin gravida nibh vel velit auctor aliquet. Aenean sollicitudin, lorem quis bibendum auctor, nisi elit consequat ipsum,</p>
  <div class="abs thumb" style="left:455px;top:563px;width:44px;height:42px;background:#e8b94a" role="img" aria-label="Photo of a learning sign"></div>
  <div class="abs" style="left:511px;top:565px;width:180px"><div class="link">Lorem Ipsum. Proin gravida nibh vel velit auctor aliquet. Aenean sollicitudin.</div><div class="date" style="margin-top:6px">July 19, 2013</div></div>
  <div class="abs" style="left:453px;top:615px;width:236px;height:1px;background:var(--line)"></div>
  <div class="abs thumb" style="left:455px;top:622px;width:44px;height:42px;background:#e9b07a" role="img" aria-label="Photo of a child with face paint"></div>
  <div class="abs" style="left:511px;top:624px;width:180px"><div class="link">Lorem Ipsum. Proin gravida nibh vel velit auctor aliquet. Aenean sollicitudin.</div><div class="date" style="margin-top:6px">July 19, 2013</div></div>
  <div class="abs" style="left:453px;top:673px;width:236px;height:1px;background:var(--line)"></div>
  <div class="abs thumb" style="left:455px;top:679px;width:44px;height:42px;background:#b8a48a" role="img" aria-label="Photo of children reading together"></div>
  <div class="abs" style="left:511px;top:681px;width:180px"><div class="link">Lorem Ipsum. Proin gravida nibh vel velit auctor aliquet. Aenean sollicitudin.</div><div class="date" style="margin-top:6px">July 19, 2013</div></div>
  <div class="abs btn" style="left:631px;top:718px;width:96px">Go to Forum</div>

  <!-- Marketplace -->
  <h2 class="abs section-head" style="left:445px;top:759px;width:282px">Marketplace</h2>
  <div class="abs photo" style="left:446px;top:788px;width:149px;height:84px;background:linear-gradient(90deg,#d9434a,#f2cf3a,#4c8fd0)" role="img" aria-label="Photo of jumping children in colourful clothes"></div>
  <p class="abs blurb" style="left:604px;top:792px;width:126px">Lorem Ipsum. Proin gravida nibh vel velit auctor aliquet. Aenean sollicitudin, lorem quis bibendum auctor, nisi elit consequat ipsum,</p>
  <h3 class="abs sub-head orange" style="left:446px;top:882px">Popular Products</h3>
  <div class="abs" style="left:446px;top:902px;width:62px;height:57px;background:linear-gradient(#f2a23a,#4a8ed0)" role="img" aria-label="Product photo: toy figures"></div>
  <div class="abs" style="left:518px;top:902px;width:63px;height:57px;background:linear-gradient(#f3d9c6,#e7a17a)" role="img" aria-label="Product photo: child with a toy"></div>
  <div class="abs" style="left:590px;top:902px;width:64px;height:57px;background:linear-gradient(#f4f4f4,#d63a3a)" role="img" aria-label="Product photo: letter block"></div>
  <div class="abs" style="left:664px;top:902px;width:63px;height:57px;background:linear-gradient(#f1d3d3,#d94a5e)" role="img" aria-label="Product photo: child in pink"></div>
  <div class="abs btn" style="left:620px;top:974px;width:107px">Go to Marketplace</div>
</main>

<footer>
  <div class="abs footer"></div>
  <div class="abs grass-strip" role="img" aria-label="Grass and flowers along the footer edge"></div>
  <div class="abs footer-kid" role="img" aria-label="Illustration of a boy peeking around the newsletter box"></div>
  <div class="abs newsletter">
    <h4>Newsletter Subscribe</h4>
    <div class="input"></div>
    <div class="submit">SUBMIT</div>
  </div>
  <div class="abs foot-col" style="left:323px;top:1046px">
    <h5>Information</h5>
    <p>About Us</p><p>Delivery Information</p><p>Privacy Policy</p><p>Terms &amp; Conditions</p>
  </div>
  <div class="abs foot-col" style="left:439px;top:1046px">
    <h5>Customer Services</h5>
    <p>Contact Us</p><p>Returns</p><p>Site Map</p>
  </div>
  <div class="abs likebox">
    <div class="top"><div class="mini"></div><div><b>TotHaven</b><div class="like-btn">Like</div></div></div>
    <div class="count">1,800 people like <em>TotHaven</em></div>
    <div class="faces" role="img" aria-label="Member avatars"><i></i><i></i><i></i><i></i><i></i><i></i><i></i><i></i><i></i><i></i></div>
  </div>
  <div class="abs copyright">© Copyright 2013, TotHaven</div>
</footer>
</body>
</html>
```